brell carpentry & property maintenance

busines card for my carpentry business
easy to read
not to bogged out with to much info
I like the colour bule baby blue ish
repair it build it fix it
all aspects of carpentry and joinery
building work no job to small

Project Deadline Extended
Reason: I can not seem to get my logo to you guys could I have an email address please to send to thanks tobias

Target Market(s)

home owners unit blocks people to busy to look after yard

Industry/Entity Type

Property Maintenance

Contact Information for Business Card

email: brellcarpentry@mailvine.com.au
phone 0427351846
Tobias Brell qualified carpenter

Logo Text

brell carpentry $ property mainteaince

Logo styles of interest
Lettermark Logo
Requirements
Must have
• thinking logo front and back a blue print type sketch plans over card
would like logo to have B T like the one that I have on my file
I can not get the look n feel tool bare to work but it should be pointing more to the pro bold up market theme
my lic no 684213c
my name Tobias Brell qualified carpenter
fully insured
Nice to have
• front int BT with Brell carpentry & property maintenance written through

```html
<!DOCTYPE html>
<html lang="en">
<head>
<meta charset="utf-8">
<title>Brell Carpentry – Business Card</title>
<link href="https://fonts.googleapis.com/css2?family=Lato:wght@300;400&display=swap" rel="stylesheet">
<style>
  :root {
    --ink: #2b2b38;
    --navy: #252848;
    --text-grey: #5a5a5a;
    --soft-grey: #b5b5b5;
    --blue: #1a9fd6;
    --blue-mid: #8fcbe2;
    --blue-pale: #d8ebf2;
    --paper: #ffffff;
  }
  html, body {
    margin: 0;
    padding: 0;
    overflow: hidden;
    background: var(--paper);
  }
  .card {
    position: relative;
    width: 694px;
    height: 1200px;
    background: var(--paper);
    font-family: "Lato", sans-serif;
    font-weight: 300;
    overflow: hidden;
  }
  .brand {
    position: absolute;
    left: 63px;
    top: 60px;
    display: flex;
    align-items: center;
    gap: 18px;
  }
  .brand-square {
    width: 96px;
    height: 96px;
    background: var(--navy);
  }
  .brand-name {
    margin: 0;
    color: var(--navy);
    font-weight: 400;
    font-size: 22px;
    line-height: 1.25;
  }
  .stripe {
    position: absolute;
    top: 266px;
    left: 0;
    width: 694px;
    height: 13px;
    display: flex;
  }
  .stripe span { display: block; height: 100%; }
  .stripe .pale { width: 227px; background: var(--blue-pale); }
  .stripe .mid  { width: 236px; background: var(--blue-mid); }
  .stripe .bold { width: 231px; background: var(--blue); }
  .contact {
    position: absolute;
    left: 57px;
    top: 948px;
    margin: 0;
    font-size: 27px;
    line-height: 47.5px;
    color: var(--text-grey);
  }
  .contact p { margin: 0; white-space: nowrap; }
  .contact .name { color: var(--ink); font-weight: 400; }
  .contact .label { color: var(--blue); font-weight: 400; }
  .contact .tagline { color: var(--soft-grey); }
</style>
</head>
<body>
  <div class="card">
    <header class="brand">
      <div class="brand-square"></div>
      <p class="brand-name">brell carpentry<br>&amp; property maintenance</p>
    </header>

    <div class="stripe" aria-hidden="true">
      <span class="pale"></span><span class="mid"></span><span class="bold"></span>
    </div>

    <address class="contact">
      <p><span class="name">Tobias Brell</span> fully insured qualified carpenter</p>
      <p><span class="label">telephone:</span> 0427351846</p>
      <p><span class="label">email:</span> brellcarpentry@mailvine.com.au</p>
      <p class="tagline">Covering all aspects of carpentry and joinery</p>
    </address>
  </div>
</body>
</html>
```